Frozen Yoghurt
Aufgabenstellung
Es soll eine Postkarte erstellt werden
auf die Vorteile des Produkts dargestellt werden
- kein fett (98% fettfrei)
- keine künstlichen süssungsmittel
- low calorien
- Viel Calcium
- Viel Eiweiss
- Vitamine durch Frucht topping
Die Postkarte soll gleichzeitig dazu dienen dass man sie mit zu uns ins Geschäft bringt und dann ein gratis Muster bekommt.
Mitbewerber: www.iwantaquirl.com, www.bluemaple.com

```html
<!DOCTYPE html>
<html lang="de">
<head>
<meta charset="utf-8">
<title>Frozen Joghurt Postkarte</title>
<link rel="stylesheet" href="https://fonts.googleapis.com/css2?family=Roboto:wght@400;500&family=Roboto+Condensed:wght@400;700&display=swap">
<style>
  :root {
    --sky-deep: #1f86d3;
    --sky-mid: #5cb8ec;
    --sky-light: #cdeefc;
    --paper: #f4fbff;
    --photo-light: #f1f3f5;
    --photo-shade: #dfe4ea;
    --ribbon-red: #d3141c;
    --ribbon-dark: #8e0a10;
    --star-red: #b5121b;
    --navy: #26375d;
    --alert-red: #d3141c;
    --ink: #1b1f2a;
    --white: #ffffff;
  }
  * { box-sizing: border-box; margin: 0; padding: 0; }
  html, body { width: 847px; height: 1200px; overflow: hidden; background: var(--white); }
  .card {
    position: relative;
    width: 847px;
    height: 1200px;
    overflow: hidden;
    background:
      linear-gradient(to bottom, rgba(244,251,255,0) 0%, rgba(244,251,255,0) 68%, rgba(244,251,255,0.85) 80%, var(--paper) 92%),
      radial-gradient(ellipse 70% 55% at 50% 45%, var(--sky-light) 0%, var(--sky-mid) 55%, var(--sky-deep) 100%);
    font-family: "Roboto Condensed", "Arial Narrow", sans-serif;
  }
  .headline {
    position: absolute;
    top: 28px;
    left: 0;
    width: 100%;
    text-align: center;
    color: var(--white);
    font-family: "Roboto", Arial, sans-serif;
    font-weight: 400;
    font-size: 122px;
    line-height: 122px;
    letter-spacing: -1px;
    text-shadow: 0 2px 6px rgba(0, 60, 120, 0.25);
  }
  .product-photo {
    position: absolute;
    left: 190px;
    top: 290px;
    width: 430px;
    height: 600px;
    border-radius: 40px;
    background: linear-gradient(to bottom, var(--photo-light) 0%, var(--photo-shade) 100%);
  }
  .ribbon {
    position: absolute;
    height: 58px;
    transform: rotate(-8deg);
    transform-origin: left center;
  }
  .ribbon-band {
    position: absolute;
    inset: 0;
    background: linear-gradient(to bottom, #e52128 0%, var(--ribbon-red) 60%, #b30f16 100%);
    clip-path: polygon(0 0, 100% 0, 100% 100%, 0 100%, 22px 50%);
    display: flex;
    align-items: center;
    justify-content: flex-end;
    padding-right: 18px;
    color: var(--white);
    font-weight: 700;
    font-size: 27px;
    letter-spacing: 0.5px;
  }
  .ribbon-fold {
    position: absolute;
    left: 0;
    bottom: -12px;
    width: 20px;
    height: 12px;
    background: var(--ribbon-dark);
    clip-path: polygon(0 0, 100% 0, 100% 100%);
  }
  .ribbon-band .big { font-size: 40px; margin-right: 6px; }
  .ribbon-band .note {
    font-size: 15px;
    line-height: 15px;
    font-weight: 700;
    font-style: italic;
    margin-right: auto;
    margin-left: 28px;
    text-align: center;
  }
  .r1 { left: 518px; top: 378px; width: 284px; }
  .r2 { left: 512px; top: 452px; width: 300px; }
  .r3 { left: 512px; top: 532px; width: 288px; }
  .r4 { left: 518px; top: 610px; width: 284px; }
  .r5 { left: 524px; top: 690px; width: 284px; }
  .gratis-star {
    position: absolute;
    left: 22px;
    top: 660px;
    width: 260px;
    height: 260px;
  }
  .gratis-star svg { position: absolute; inset: 0; }
  .gratis-text {
    position: absolute;
    inset: 0;
    display: flex;
    flex-direction: column;
    align-items: center;
    justify-content: center;
    transform: rotate(-14deg);
    color: var(--white);
    text-align: center;
    font-weight: 700;
  }
  .gratis-text .word { font-size: 52px; line-height: 50px; letter-spacing: 1px; }
  .gratis-text .detail { font-size: 30px; line-height: 30px; font-weight: 400; }
  .offer {
    position: absolute;
    left: 0;
    top: 912px;
    width: 100%;
    text-align: center;
    color: var(--navy);
  }
  .offer-kicker { font-size: 31px; font-weight: 700; line-height: 40px; letter-spacing: 0.5px; }
  .offer-title { font-size: 56px; font-weight: 700; line-height: 72px; letter-spacing: 1px; }
  .how-to {
    position: absolute;
    left: 0;
    top: 1088px;
    width: 100%;
    text-align: center;
  }
  .how-to-title { color: var(--alert-red); font-size: 25px; font-weight: 700; line-height: 32px; }
  .how-to-text { color: var(--ink); font-size: 24px; font-weight: 700; line-height: 32px; }
</style>
</head>
<body>
  <main class="card">
    <h1 class="headline">Auf die Löffel,<br>fertig, los.</h1>

    <div class="product-photo" role="img" aria-label="Foto: Frozen Joghurt im weißen Becher mit Beeren und Granola"></div>

    <div class="ribbon r1"><div class="ribbon-band"><span class="big">98%</span>FETTFREI</div><div class="ribbon-fold"></div></div>
    <div class="ribbon r2"><div class="ribbon-band">KEINE SÜSSSTOFFE</div><div class="ribbon-fold"></div></div>
    <div class="ribbon r3"><div class="ribbon-band">WENIG KALORIEN</div><div class="ribbon-fold"></div></div>
    <div class="ribbon r4"><div class="ribbon-band">VIEL EIWEISS</div><div class="ribbon-fold"></div></div>
    <div class="ribbon r5"><div class="ribbon-band"><span class="note">Frucht-<br>Topping</span>VIEL VITAMINE</div><div class="ribbon-fold"></div></div>

    <div class="gratis-star">
      <svg viewBox="0 0 260 260" aria-hidden="true">
        <polygon fill="var(--star-red)" points="130,4 145,38 172,12 177,50 210,32 204,70 242,62 225,96 258,106 230,130 258,154 225,164 242,198 204,190 210,228 177,210 172,248 145,222 130,256 115,222 88,248 83,210 50,228 56,190 18,198 35,164 2,154 30,130 2,106 35,96 18,62 56,70 50,32 83,50 88,12 115,38"/>
      </svg>
      <div class="gratis-text">
        <span class="word">GRATIS</span>
        <span class="detail">Frozen Joghurt-</span>
        <span class="detail">becher.</span>
      </div>
    </div>

    <section class="offer">
      <p class="offer-kicker">HOLEN SIE SICH IHREN GRATIS</p>
      <h2 class="offer-title">FROZEN JOGHURT BECHER</h2>
    </section>

    <section class="how-to">
      <p class="how-to-title">SO GEHT'S!</p>
      <p class="how-to-text">Diese Karte mit zu uns in den Shop bringen (Adresse auf der Rückseite)<br>und erhalten Sie eine Portion Frozen Joghurt frei nach Wahl.</p>
    </section>
  </main>
</body>
</html>
```